Football blog needs a Wordpress design new site

We need a wordpress design for a new football blog site. We would like to see a design that uses the colours green, white and black and one that makes good use of the slideshow widgets as scene in the site 'www.tarnwick.net'
We would like a modern and sleek looking site but one that is also professional and easy to navigate.
Unfortunately due to unforeseen circumstances we are having to shorten the deadline date for this project.
The new deadline date is 16/07/2014.
We apologise for any inconveniance
Industry/Entity Type
It Professional
Look and feel

```html
<!DOCTYPE html>
<html lang="en">
<head>
<meta charset="utf-8">
<title>Sideline Chatter – Football Blog</title>
<link href="https://fonts.googleapis.com/css2?family=Lato:ital,wght@0,300;0,400;0,700;0,900;1,400;1,700&family=Roboto+Condensed:wght@400;700&display=swap" rel="stylesheet">
<style>
:root{
  --green:#3ab54a;
  --green-dark:#2e9a3c;
  --black:#0c0c0c;
  --panel:#151515;
  --white:#ffffff;
  --grey:#8a8a8a;
  --grey-light:#d6d6d6;
  --text:#333333;
  --gold:#b8860b;
}
*{box-sizing:border-box;margin:0;padding:0}
html,body{width:1200px;height:2571px;overflow:hidden}
body{position:relative;font-family:"Lato",Arial,sans-serif;color:var(--text);background:var(--black)}
.abs{position:absolute}
a{color:inherit;text-decoration:none}

/* header */
.site-header{position:absolute;left:0;top:0;width:1200px;height:200px;background:var(--white)}
.brand{position:absolute;left:43px;top:22px;width:170px;text-align:left}
.brand-mark{display:block;width:110px;height:110px;border-radius:50%;background:var(--green);margin-left:26px}
.brand-name{display:block;margin-top:14px;font-weight:700;font-size:23px;color:var(--green);white-space:nowrap}
.social{position:absolute;left:820px;top:43px;display:flex;gap:16px}
.social span{width:34px;height:34px;background:#e9e9e9;border:1px solid #d8d8d8;display:block}
.social span.primary{background:#3b5fa0;border-color:#3b5fa0}
.search{position:absolute;left:821px;top:111px;width:331px;height:45px;border:3px solid var(--green);display:flex}
.search input{flex:1;border:0;padding-left:12px;font:italic 14px "Lato",sans-serif;color:#999;outline:none}
.search button{width:45px;border:0;background:var(--green);display:flex;align-items:center;justify-content:center}

/* pitch background */
.pitch{position:absolute;left:0;top:200px;width:1200px;height:2161px;
  background:linear-gradient(180deg,#13240c 0%,#274d18 18%,#2f5c1e 35%,#203f14 55%,#111f0b 75%,#0d130a 100%)}

/* hero */
.hero{position:absolute;left:45px;top:200px;width:1110px;height:491px;
  background:linear-gradient(135deg,#1d2a12 0%,#6b5a1a 35%,#c9a52a 55%,#3b3a1c 80%,#0f140c 100%)}
.main-nav{position:absolute;left:45px;top:200px;width:1110px;height:57px;background:rgba(0,0,0,.78);display:flex}
.main-nav a{color:var(--white);font:700 17px "Lato",sans-serif;text-transform:uppercase;line-height:57px;padding:0 18px}
.main-nav a.active{background:var(--green)}
.main-nav a:nth-child(2){margin-left:4px}
.hero-tags{position:absolute;left:55px;top:591px;display:flex;gap:6px}
.tag{font:700 11px "Lato",sans-serif;text-transform:uppercase;color:var(--white);padding:5px 9px;background:var(--black)}
.tag.green{background:var(--green)}
.tag.gold{background:var(--gold)}
.hero-caption{position:absolute;left:45px;top:626px;width:1110px;height:65px;background:rgba(0,0,0,.65);
  color:var(--white);font:300 28px "Lato",sans-serif;line-height:65px;padding-left:20px;white-space:nowrap}

/* section headings */
.section-head{position:absolute;height:46px;background:var(--black);color:var(--green);
  font:700 20px "Roboto Condensed",sans-serif;text-transform:uppercase;line-height:46px;padding-left:20px}
.dots{position:absolute;right:18px;top:20px;display:flex;gap:6px}
.dots i{width:6px;height:6px;border-radius:50%;background:#777;display:block}
.dots i:first-child{background:var(--green)}
.panel{position:absolute;background:var(--white)}
.photo{position:absolute}

/* event cards */
.event{position:absolute;top:780px;width:219px}
.event .photo{left:0;top:0;width:219px;height:132px}
.event .label{position:absolute;left:0;top:100px;width:110px;height:32px;background:var(--green);
  color:var(--white);font:italic 700 16px "Lato",sans-serif;line-height:32px;padding-left:10px}
.event h3{position:absolute;top:146px;font:400 14px "Lato",sans-serif;color:#222;white-space:nowrap}
.event h3.hl{color:var(--green)}
.event .meta{position:absolute;top:182px;font:13px "Lato",sans-serif;color:#444;display:flex;gap:22px;white-space:nowrap}
.meta svg{vertical-align:-2px;margin-right:5px}

/* popular */
.popular-caption{position:absolute;left:62px;top:1252px;width:341px;height:42px;background:rgba(0,0,0,.6);
  color:var(--white);font:400 20px "Lato",sans-serif;line-height:42px;padding-left:16px}

/* chatter feature */
.feature-meta{position:absolute;left:62px;top:1846px;font:13px "Lato",sans-serif;color:#222;display:flex;gap:42px;text-transform:uppercase}
.feature-title{position:absolute;left:62px;top:1878px;width:340px;font:400 19px/1.5 "Lato",sans-serif;color:var(--green)}
.feature-tags{position:absolute;left:62px;top:1950px;display:flex;gap:6px}
.feature-text{position:absolute;left:62px;top:1986px;width:340px;font:13px/1.65 "Lato",sans-serif;color:#888}
.mini{position:absolute;left:430px;width:330px;height:110px}
.mini .photo{left:0;top:0;width:141px;height:110px}
.mini h4{position:absolute;left:153px;top:-4px;width:160px;font:400 16px/1.35 "Lato",sans-serif;color:#222}
.mini h4.hl{color:var(--green)}
.mini .author{position:absolute;left:153px;top:58px;font:italic 12px "Lato",sans-serif;color:#999;text-transform:uppercase}
.mini .date{position:absolute;left:153px;top:90px;font:12px "Lato",sans-serif;color:#222}

/* sidebar news */
.news{position:absolute;left:814px;width:341px;height:100px;background:var(--white)}
.news .photo{top:0;width:146px;height:100px}
.news .text{position:absolute;top:16px;width:180px}
.news .date{font:italic 700 13px "Lato",sans-serif;color:#222}
.news .title{font:400 14px "Lato",sans-serif;color:var(--green);margin-top:8px;white-space:nowrap}
.news .more{font:italic 12px "Lato",sans-serif;color:#999;margin-top:10px}
.news.lead{background:#0e0e0e}
.news.lead .date,.news.lead .more{color:var(--white)}
.news.lead .more{font-weight:700}

.story{position:absolute;left:814px;width:341px;height:98px;background:var(--white)}
.story .photo{left:0;top:0;width:115px;height:98px}
.story h4{position:absolute;left:127px;top:14px;font:400 14px "Lato",sans-serif;color:#222;white-space:nowrap}
.story p{position:absolute;left:127px;top:40px;width:205px;font:13px/1.45 "Lato",sans-serif;color:#777}
.story.lead{background:rgba(10,20,8,.85)}
.story.lead h4{color:var(--green)}
.story.lead p{color:#bbb}

.sponsor-row{display:flex;justify-content:space-around;align-items:center;height:72px;padding:0 10px}
.sponsor-row span{width:48px;height:48px;border-radius:50%;display:block}

/* footer */
.site-footer{position:absolute;left:0;top:2361px;width:1200px;height:210px;background:#1e1e1e}
.footer-links{position:absolute;left:45px;top:30px;font:14px "Lato",sans-serif;color:#9a9a9a}
.footer-links a:first-child{color:var(--green)}
.footer-links b{font-weight:400;margin:0 6px}
.footer-name{position:absolute;left:45px;top:80px;font:700 24px "Lato",sans-serif;color:#666;white-space:nowrap}
.footer-mark{position:absolute;left:238px;top:78px;width:70px;height:70px;border-radius:50%;background:#4a4a4a}
.copyright{position:absolute;left:45px;top:128px;font:13px "Lato",sans-serif;color:#9a9a9a}
.footer-col{position:absolute;top:30px;list-style:none;font:14px "Lato",sans-serif;color:#8c8c8c}
.footer-col li{height:40px}
.footer-col li::before{content:"";display:inline-block;width:7px;height:7px;border:1px solid #777;margin-right:6px;vertical-align:1px}
.footer-col li.current{color:var(--green)}
.footer-col li.current::before{border-color:var(--green)}
</style>
</head>
<body>

<header class="site-header">
  <a class="brand" href="#"><span class="brand-mark" aria-hidden="true"></span><span class="brand-name">Sideline Chatter</span></a>
  <div class="social" aria-label="Social links">
    <span class="primary"></span><span></span><span></span><span></span><span></span><span></span><span></span>
  </div>
  <form class="search">
    <input type="text" value="Search" aria-label="Search">
    <button type="button" aria-label="Search">
      <svg width="20" height="20" viewBox="0 0 20 20"><circle cx="11" cy="8" r="6" fill="none" stroke="#fff" stroke-width="2.4"/><line x1="7" y1="12" x2="2" y2="18" stroke="#fff" stroke-width="2.6" stroke-linecap="round"/></svg>
    </button>
  </form>
</header>

<div class="pitch" role="img" aria-label="Grass pitch texture background"></div>

<section class="hero-slider">
  <div class="hero" role="img" aria-label="Photo of fans in yellow shirts celebrating with a trophy"></div>
  <nav class="main-nav">
    <a class="active" href="#">Home</a><a href="#">About us</a><a href="#">World Cup</a><a href="#">Videos</a><a href="#">Blog</a><a href="#">Write for us</a><a href="#">Writers</a><a href="#">Shop</a><a href="#">Contct us</a>
  </nav>
  <div class="hero-tags"><span class="tag green">Top Tuchline</span><span class="tag">Lifestyle</span><span class="tag gold">Woldcup</span></div>
  <div class="hero-caption">Lorem ipsum dolor sit amet consectetur adipiscing elit curabitur lorem ante</div>
</section>

<!-- main column -->
<h2 class="section-head" style="left:45px;top:715px;width:737px">Latest Events<span class="dots"><i></i><i></i><i></i><i></i><i></i><i></i><i></i></span></h2>
<div class="panel" style="left:45px;top:761px;width:737px;height:250px"></div>
<article class="event" style="left:62px">
  <div class="photo" role="img" aria-label="Photo of a football match tackle" style="background:linear-gradient(135deg,#2f6a26,#c9b640 60%,#3a7a2c)"></div>
  <span class="label">Football</span>
  <h3 class="hl">Lorem ipsum dolor sit .</h3>
  <div class="meta"><span><svg width="11" height="11" viewBox="0 0 12 12"><circle cx="6" cy="6" r="5" fill="none" stroke="#666" stroke-width="1.3"/><path d="M6 3v3h2.5" fill="none" stroke="#666" stroke-width="1.3"/></svg>1:40 pm</span><span><svg width="11" height="11" viewBox="0 0 12 12"><rect x="1" y="2" width="10" height="9" fill="none" stroke="#666" stroke-width="1.3"/><line x1="1" y1="5" x2="11" y2="5" stroke="#666" stroke-width="1.3"/></svg>25 Nov 2013</span></div>
</article>
<article class="event" style="left:304px">
  <div class="photo" role="img" aria-label="Photo of a flag, match ball and trophy" style="background:linear-gradient(135deg,#2a7a36,#d4c23a 50%,#1d4f9a)"></div>
  <span class="label">Football</span>
  <h3>Lorem ipsum dolor sit .</h3>
  <div class="meta"><span><svg width="11" height="11" viewBox="0 0 12 12"><circle cx="6" cy="6" r="5" fill="none" stroke="#666" stroke-width="1.3"/><path d="M6 3v3h2.5" fill="none" stroke="#666" stroke-width="1.3"/></svg>1:40 pm</span><span><svg width="11" height="11" viewBox="0 0 12 12"><rect x="1" y="2" width="10" height="9" fill="none" stroke="#666" stroke-width="1.3"/><line x1="1" y1="5" x2="11" y2="5" stroke="#666" stroke-width="1.3"/></svg>25 Nov 2013</span></div>
</article>
<article class="event" style="left:545px">
  <div class="photo" role="img" aria-label="Photo of a coach on the phone at pitchside" style="background:linear-gradient(135deg,#3f8a34,#253248 55%,#4a8c3a)"></div>
  <span class="label">Football</span>
  <h3>Lorem ipsum dolor sit .</h3>
  <div class="meta"><span><svg width="11" height="11" viewBox="0 0 12 12"><circle cx="6" cy="6" r="5" fill="none" stroke="#666" stroke-width="1.3"/><path d="M6 3v3h2.5" fill="none" stroke="#666" stroke-width="1.3"/></svg>1:40 pm</span><span><svg width="11" height="11" viewBox="0 0 12 12"><rect x="1" y="2" width="10" height="9" fill="none" stroke="#666" stroke-width="1.3"/><line x1="1" y1="5" x2="11" y2="5" stroke="#666" stroke-width="1.3"/></svg>25 Nov 2013</span></div>
</article>

<h2 class="section-head" style="left:45px;top:1027px;width:737px">Most Populer<span class="dots"><i></i><i></i><i></i><i></i><i></i><i></i><i></i></span></h2>
<div class="panel" style="left:45px;top:1073px;width:737px;height:463px"></div>
<div class="photo" role="img" aria-label="Photo of a fan waving a flag" style="left:62px;top:1094px;width:341px;height:200px;background:linear-gradient(135deg,#3c6e2c,#c7b76a 50%,#2f5a26)"></div>
<div class="hero-tags" style="left:70px;top:1104px"><span class="tag green">Top Tuchline</span><span class="tag">Lifestyle</span></div>
<div class="popular-caption">Top 10 World Cup WAGs</div>
<div class="photo" role="img" aria-label="Photo of fans in blue shirts cheering" style="left:423px;top:1094px;width:342px;height:200px;background:linear-gradient(135deg,#4a5a3a,#1f4fa0 55%,#c9a04a)"></div>
<div class="photo" role="img" aria-label="Photo of two fans in yellow and blue hats" style="left:62px;top:1317px;width:341px;height:202px;background:linear-gradient(135deg,#1d3c8a,#e0c23a 45%,#b07a56)"></div>
<div class="photo" role="img" aria-label="Photo of a fan with face paint" style="left:423px;top:1317px;width:342px;height:202px;background:linear-gradient(135deg,#2a6ac0,#7aa8d8 55%,#2a4a70)"></div>

<h2 class="section-head" style="left:45px;top:1572px;width:737px">The Sideline Chatter<span class="dots"><i></i><i></i><i></i><i></i><i></i><i></i><i></i></span></h2>
<div class="panel" style="left:45px;top:1618px;width:737px;height:456px"></div>
<div class="photo" role="img" aria-label="Photo of a player in a yellow shirt consoled by a child" style="left:62px;top:1639px;width:351px;height:192px;background:linear-gradient(135deg,#b77a52,#e3c33a 50%,#2f6a2a)"></div>
<div class="feature-meta"><span>Lorem Ispum</span><span>July 11, 2014</span></div>
<h3 class="feature-title">Lorem ipsum dolor sit amet, coctetur adipiscing elit</h3>
<div class="feature-tags"><span class="tag green">Top Tuchline</span><span class="tag">Lifestyle</span></div>
<p class="feature-text">Donec non interdum risus. Duis porta luctus mi eget porta. Morbi lacinia neque sit amet vehic tum Donec non interdum risusla tum</p>

<article class="mini" style="top:1644px">
  <div class="photo" role="img" aria-label="Photo of players in yellow shirts" style="background:linear-gradient(135deg,#c99a3a,#e0c43a 50%,#3a6a2a)"></div>
  <h4 class="hl">Lorem ipsum dolor sit amet consectetur</h4>
  <span class="author">Marcusweller</span><span class="date">JULY 10, 2014</span>
</article>
<article class="mini" style="top:1778px">
  <div class="photo" role="img" aria-label="Photo of players in yellow shirts" style="background:linear-gradient(135deg,#a87a4a,#d8bc3a 50%,#35662a)"></div>
  <h4>Lorem ipsum dolor sit amet consectetur</h4>
  <span class="author">Marcusweller</span><span class="date">JULY 10, 2014</span>
</article>
<article class="mini" style="top:1911px">
  <div class="photo" role="img" aria-label="Photo of fans at a stadium" style="background:linear-gradient(135deg,#3a5a7a,#c05050 50%,#3a6a3a)"></div>
  <h4>Lorem ipsum dolor sit amet consectetur</h4>
  <span class="author">Marcusweller</span><span class="date">JULY 10, 2014</span>
</article>

<h2 class="section-head" style="left:45px;top:2108px;width:737px">Latest Video<span class="dots"><i></i><i></i><i></i><i></i><i></i><i></i><i></i></span></h2>
<div class="panel" style="left:45px;top:2154px;width:737px;height:172px"></div>
<div class="photo" role="img" aria-label="Video still of a football match" style="left:62px;top:2177px;width:219px;height:132px;background:linear-gradient(135deg,#1a3a14,#4a5a2a 55%,#1d3516)"></div>
<svg class="abs" style="left:145px;top:2217px" width="52" height="52" viewBox="0 0 52 52" aria-hidden="true"><circle cx="26" cy="26" r="23" fill="none" stroke="#3ab54a" stroke-width="3.5"/><path d="M21 16l14 10-14 10z" fill="#3ab54a"/></svg>
<div class="photo" role="img" aria-label="Video still of a flag, ball and trophy" style="left:304px;top:2177px;width:219px;height:132px;background:linear-gradient(135deg,#2a7a36,#d4c23a 50%,#1d4f9a)"></div>
<div class="photo" role="img" aria-label="Video still of a coach on the phone" style="left:545px;top:2177px;width:220px;height:132px;background:linear-gradient(135deg,#3f8a34,#253248 55%,#4a8c3a)"></div>

<!-- sidebar -->
<h2 class="section-head" style="left:814px;top:715px;width:341px">Latest News</h2>
<article class="news lead" style="top:763px">
  <div class="photo" role="img" aria-label="Photo of a player celebrating on his knees" style="left:0;background:linear-gradient(135deg,#3a7a2c,#2a3c8a 55%,#9a2a3a)"></div>
  <div class="text" style="left:160px"><div class="date">JUL 10, 2014</div><div class="title">Lorem ispum dolor amet</div><div class="more">Read more</div></div>
</article>
<article class="news" style="top:866px">
  <div class="text" style="left:16px"><div class="date">JUL 10, 2014</div><div class="title">Lorem ispum dolor amet</div><div class="more">Read more</div></div>
  <div class="photo" role="img" aria-label="Photo of a player in a white kit" style="left:195px;background:linear-gradient(135deg,#4a7a3a,#e8e8e8 55%,#3a6a2a)"></div>
</article>
<article class="news" style="top:969px">
  <div class="text" style="left:16px"><div class="date">JUL 10, 2014</div><div class="title">Lorem ispum dolor amet</div><div class="more">Read more</div></div>
  <div class="photo" role="img" aria-label="Photo of a player in a striped kit" style="left:195px;background:linear-gradient(135deg,#3a7a2c,#c83a3a 55%,#2f6a26)"></div>
</article>
<article class="news" style="top:1072px">
  <div class="text" style="left:16px"><div class="date">JUL 10, 2014</div><div class="title">Lorem ispum dolor amet</div><div class="more">Read more</div></div>
  <div class="photo" role="img" aria-label="Photo of players competing for the ball" style="left:195px;background:linear-gradient(135deg,#1a2a5a,#b03030 55%,#2a5a22)"></div>
</article>
<article class="news" style="top:1175px">
  <div class="text" style="left:16px"><div class="date">JUL 10, 2014</div><div class="title">Lorem ispum dolor amet</div><div class="more">Read more</div></div>
  <div class="photo" role="img" aria-label="Photo of players in a tackle" style="left:195px;background:linear-gradient(135deg,#3a7a2c,#d8b83a 50%,#a02a2a)"></div>
</article>

<h2 class="section-head" style="left:814px;top:1298px;width:341px">The Bollocks</h2>
<article class="story lead" style="top:1347px">
  <div class="photo" role="img" aria-label="Photo of players in blue shirts" style="background:linear-gradient(135deg,#1f3f8a,#c9a03a 55%,#2a5a2a)"></div>
  <h4>Lorem ispum dolor amet</h4><p>Proin ornare augue purus, eu cursus nibh vestibulum quis.</p>
</article>
<article class="story" style="top:1449px">
  <div class="photo" role="img" aria-label="Photo of a trophy presentation" style="background:linear-gradient(135deg,#2a4a2a,#c9a52a 55%,#3a3a3a)"></div>
  <h4>Lorem ispum dolor amet</h4><p>Proin ornare augue purus, eu cursus nibh vestibulum quis.</p>
</article>
<article class="story" style="top:1551px">
  <div class="photo" role="img" aria-label="Photo of players on a pitch" style="background:linear-gradient(135deg,#2a2a4a,#8a2a3a 55%,#2a5a2a)"></div>
  <h4>Lorem ispum dolor amet</h4><p>Proin ornare augue purus, eu cursus nibh vestibulum quis.</p>
</article>

<div class="photo" role="img" aria-label="Advertisement for a games console with a controller" style="left:814px;top:1680px;width:341px;height:245px;background:linear-gradient(160deg,#1c6ad0,#0d3f94 55%,#0a1a3a)"></div>
<div class="photo" role="img" aria-label="Photo of an opening ceremony in a stadium" style="left:814px;top:1959px;width:341px;height:213px;background:linear-gradient(180deg,#c8b88a,#6a5a3a 40%,#2a6a2a 75%,#b02a2a)"></div>

<h2 class="section-head" style="left:820px;top:2206px;width:335px">Our Sponsors<span class="dots"><i></i><i></i><i></i><i></i><i></i><i></i><i></i></span></h2>
<div class="panel sponsor-row" style="left:820px;top:2253px;width:335px" aria-label="Sponsor badges">
  <span style="background:#1f3a7a"></span><span style="background:#d8b84a"></span><span style="background:#2a7ac0"></span><span style="background:#c8282e"></span><span style="background:#e04a2a"></span>
</div>

<footer class="site-footer">
  <div class="footer-links"><a href="#">Home</a><b>/</b><a href="#">About us</a><b>/</b><a href="#">Tournaments</a><b>/</b><a href="#">Contacts</a></div>
  <span class="footer-name">Sideline Chatter</span>
  <span class="footer-mark" aria-hidden="true"></span>
  <div class="copyright">© 2014 | Privacy Policy</div>
  <ul class="footer-col" style="left:533px"><li class="current">News</li><li>Tournaments</li><li>Teams</li><li>Training</li></ul>
  <ul class="footer-col" style="left:782px"><li>Equipment</li><li>Recruiting</li><li>Recruiting Camps</li><li>Services</li></ul>
  <ul class="footer-col" style="left:1047px"><li>Calendar</li><li>Clinics</li><li>Photo Album</li><li>Our Sponsors</li></ul>
</footer>

</body>
</html>
```